Lumen Path - Fiber Internet to the home postcard

Design a postcard for my company, Lumen Path, using the logo below. On the front of the card:
- No Buffering • No BS
- Second line should be the logo
- $60 / month • 10-Gigs
- lumenpath.net

Color palate should follow the colors in the logo.

Address should say
- Special pricing during construction
- Our best price
- Our fastest speed
- $60 / month • 10-Gigs
- lumenpath.net

Target Market(s)

25 - 55 year olds. Middle income/class. People with kids and pick up trucks

Industry/Entity Type

Fiber Internet Service Provider

Font styles to use
Sans Serif

Colors

Designer to choose colors to be used in the design.

Requirements
Nice to have
• I am open to more creative changes

```html
<!DOCTYPE html>
<html lang="en">
<head>
<meta charset="utf-8">
<title>Lumen Path – Fiber Postcard</title>
<link rel="stylesheet" href="https://fonts.googleapis.com/css2?family=Montserrat:wght@700;800&family=Bebas+Neue&display=swap">
<style>
  :root {
    --navy: #002a5c;
    --green: #7ac143;
    --panel: #eeeef2;
    --white: #ffffff;
    --fiber-deep: #2a1a7a;
    --fiber-blue: #2f6fe0;
    --fiber-violet: #7a3fd0;
    --fiber-pink: #d45aa8;
  }
  * { margin: 0; padding: 0; box-sizing: border-box; }
  html, body { width: 1200px; height: 927px; overflow: hidden; background: var(--white); }
  .postcard {
    position: relative;
    width: 1200px;
    height: 927px;
    font-family: "Montserrat", sans-serif;
    overflow: hidden;
  }
  .fiber-backdrop {
    position: absolute;
    inset: 0;
    background:
      radial-gradient(circle at 15% 20%, rgba(212,90,168,.55), transparent 30%),
      radial-gradient(circle at 85% 30%, rgba(47,111,224,.6), transparent 35%),
      radial-gradient(circle at 20% 90%, rgba(212,90,168,.5), transparent 30%),
      radial-gradient(circle at 80% 90%, rgba(47,111,224,.55), transparent 35%),
      linear-gradient(160deg, var(--fiber-violet), var(--fiber-deep) 50%, var(--fiber-blue));
  }
  .content-panel {
    position: absolute;
    left: 68px;
    top: 89px;
    width: 1064px;
    height: 746px;
    background: var(--panel);
    border-radius: 12px;
    overflow: hidden;
  }
  .tagline {
    position: absolute;
    top: 50px;
    width: 100%;
    text-align: center;
    font-weight: 800;
    font-size: 61px;
    line-height: 72px;
    color: var(--navy);
    letter-spacing: 0.5px;
  }
  .dot { color: var(--green); }
  .brand {
    position: absolute;
    top: 150px;
    width: 100%;
    height: 290px;
    display: flex;
    justify-content: center;
    align-items: center;
  }
  .brand-name {
    font-weight: 800;
    font-size: 132px;
    line-height: 1;
    color: var(--navy);
    letter-spacing: -2px;
  }
  .offer {
    position: absolute;
    top: 470px;
    width: 100%;
    text-align: center;
    font-weight: 800;
    font-size: 64px;
    line-height: 76px;
    color: var(--navy);
  }
  .offer .price { color: var(--green); }
  .promo-band {
    position: absolute;
    left: 0;
    top: 571px;
    width: 100%;
    height: 100px;
    background: var(--green);
    color: var(--white);
    font-family: "Bebas Neue", sans-serif;
    font-size: 84px;
    line-height: 100px;
    text-align: center;
    letter-spacing: 0.5px;
  }
  .benefits {
    position: absolute;
    left: 0;
    top: 671px;
    width: 100%;
    height: 75px;
    background: var(--white);
    font-weight: 800;
    font-size: 26px;
    line-height: 75px;
    text-align: center;
    color: var(--navy);
  }
  .benefits .price { color: var(--green); }
  .web-address {
    position: absolute;
    top: 856px;
    width: 100%;
    text-align: center;
    font-weight: 800;
    font-size: 32px;
    color: var(--white);
  }
</style>
</head>
<body>
  <main class="postcard">
    <div class="fiber-backdrop" role="img" aria-label="Glowing fiber optic strands in blue, violet and pink"></div>

    <section class="content-panel">
      <h2 class="tagline">NO BUFFERING <span class="dot">•</span> NO BS</h2>

      <div class="brand">
        <h1 class="brand-name">Lumen Path</h1>
      </div>

      <p class="offer"><span class="price">$60 / MONTH</span> • 10-GIGS</p>

      <div class="promo-band">SPECIAL PRICING DURING CONSTRUCTION</div>

      <p class="benefits">OUR BEST PRICE <span class="dot">•</span> OUR FASTEST SPEED <span class="dot">•</span> <span class="price">$60 / MONTH</span> <span class="dot">•</span> 10-GIGS</p>
    </section>

    <p class="web-address">lumenpath.net</p>
  </main>
</body>
</html>
```